A online shop for solid wood need a Stationary design

A new online shop (in Austria and Germany) for solid wood and steel furniture (feldberg-formwerk) needs a Stationay design (letterhead, business card, envelope etc...). Dining tables, coffee tables, TV furniture and similar furniture will be sold. Everything will be custom made.

```html
<!DOCTYPE html>
<html lang="en">
<head>
<meta charset="utf-8">
<title>Feldberg Formwerk – Business Card</title>
<link rel="stylesheet" href="https://fonts.googleapis.com/css2?family=Montserrat:wght@600;700&family=Arimo:wght@400&display=swap">
<style>
  :root {
    --stage: #262626;
    --card: #0b0b0b;
    --accent: #e61e26;
    --text: #e9e9e9;
    --muted: #bdbdbd;
    --divider: #2e2e2e;
  }
  * { box-sizing: border-box; margin: 0; padding: 0; }
  html, body { width: 1200px; height: 900px; overflow: hidden; }
  body {
    background: var(--stage);
    display: flex;
    flex-direction: column;
    align-items: center;
    justify-content: center;
    gap: 40px;
    font-family: "Arimo", Arial, sans-serif;
  }
  .card {
    width: 700px;
    height: 400px;
    background: var(--card);
    position: relative;
    box-shadow: 0 10px 30px rgba(0,0,0,.5);
  }
  .wordmark {
    display: flex;
    align-items: center;
    gap: 18px;
    font-family: "Montserrat", Arial, sans-serif;
    font-weight: 700;
    color: var(--accent);
    text-transform: uppercase;
    line-height: 1.05;
  }
  .wordmark-square {
    width: 64px; height: 64px;
    background: var(--accent);
    flex-shrink: 0;
  }
  .wordmark-name { font-size: 38px; letter-spacing: 2px; }

  /* Front */
  .card-front { display: flex; }
  .front-brand {
    width: 46%;
    display: flex;
    align-items: center;
    justify-content: center;
    border-right: 1px solid var(--divider);
    margin: 40px 0;
  }
  .front-brand .wordmark-name { font-size: 28px; }
  .front-brand .wordmark-square { width: 44px; height: 44px; }
  .front-contact {
    flex: 1;
    padding: 72px 0 0 44px;
    color: var(--text);
  }
  .person-name {
    font-family: "Montserrat", Arial, sans-serif;
    font-weight: 600;
    font-size: 24px;
    color: var(--accent);
    text-transform: uppercase;
    letter-spacing: .5px;
  }
  .person-role { font-size: 18px; margin-top: 4px; }
  .contact-list { list-style: none; margin-top: 22px; }
  .contact-list li {
    display: flex; align-items: center; gap: 10px;
    font-size: 18px; line-height: 1.45;
  }
  .contact-list svg { width: 16px; height: 16px; fill: var(--accent); flex-shrink: 0; }
  .highlight { color: var(--accent); }
  .address { font-size: 18px; line-height: 1.4; margin-top: 22px; margin-left: 26px; color: var(--text); }

  /* Back */
  .card-back { display: flex; align-items: center; justify-content: center; }
</style>
</head>
<body>

<section class="card card-front">
  <div class="front-brand">
    <div class="wordmark">
      <span class="wordmark-square"></span>
      <span class="wordmark-name">Feldberg<br>Formwerk</span>
    </div>
  </div>
  <div class="front-contact">
    <h1 class="person-name">Lukas Brenner</h1>
    <p class="person-role">Managing Director</p>
    <ul class="contact-list">
      <li>
        <svg viewBox="0 0 16 16" aria-hidden="true"><path d="M3.6 1.2l2.3 2.6-1.3 1.8c.9 2 2.4 3.5 4.4 4.4l1.8-1.3 2.6 2.3-1.4 2.4C6.6 13.1 2.9 9.4 1.2 3.6z"/></svg>
        043-918 270 564
      </li>
      <li>
        <svg viewBox="0 0 16 16" aria-hidden="true"><path d="M1 3h14v10H1z M2 4.2v.4l6 4.2 6-4.2v-.4z" fill-rule="evenodd"/></svg>
        info@feldberg-formwerk.com
      </li>
      <li>
        <svg viewBox="0 0 16 16" aria-hidden="true"><path d="M8 1a7 7 0 100 14A7 7 0 008 1zm0 1.4c.8.8 1.5 2.2 1.7 3.9H6.3C6.5 4.6 7.2 3.2 8 2.4zM2.5 7.3h2.8c0 .5 0 1 .1 1.4H2.5a5.6 5.6 0 010-1.4zm3.9 0h3.2a9 9 0 010 1.4H6.4a9 9 0 010-1.4zm4.3 0h2.8a5.6 5.6 0 010 1.4h-2.8c.1-.4.1-.9 0-1.4zM6.3 9.7h3.4c-.2 1.7-.9 3.1-1.7 3.9-.8-.8-1.5-2.2-1.7-3.9z"/></svg>
        www.<span class="highlight">feldberg-formwerk</span>.com
      </li>
    </ul>
    <p class="address">421, Address line goes here<br>45452, Country Name</p>
  </div>
</section>

<section class="card card-back">
  <div class="wordmark">
    <span class="wordmark-square"></span>
    <span class="wordmark-name">Feldberg<br>Formwerk</span>
  </div>
</section>

</body>
</html>
```